Flyer Tally Your Ledger Free

Hi
Can you please design me a DL Flyer for: Tally Your Ledger Free
Info:
Starting a new Business ?
Want to save on bookkeeping fees for your existing business?

You can now save 1000's off bookkeeping fees by Doing it Yourself.

Using our Bookkeeper software you simply key in the information as you go.

We offer one on one training, backup and support.
We can assist you with BAS Preparation and Payrol Advice.

Add Modules as required:
Point of Sale Module
Jobs Management Module
Website Intergration Module

Fee set up assistance and training.

Lets get the ball rolling: 1300 642 815
www.tylfr.com.au
admin@tylfr.com.au (use the logo thing you made)

Target Market(s)

Small Business

Colors
ec1f27
f04a50
f59296
fcdcdc
ffffff

Requirements
Nice to have
• image/s related to bookkeeping

```html
<!DOCTYPE html>
<html lang="en">
<head>
<meta charset="utf-8">
<title>Tally Your Ledger Free – DL Flyer</title>
<link rel="stylesheet" href="https://fonts.googleapis.com/css2?family=Montserrat:wght@500&family=Lora:ital@1&family=Roboto:wght@500&family=Open+Sans:wght@400;500&family=Quicksand:wght@700&display=swap">
<style>
  :root {
    --red: #ec1f27;
    --red-soft: #f04a50;
    --pink: #f59296;
    --blush: #fcdcdc;
    --white: #ffffff;
    --paper: #e9eaee;
    --ink: #2b2b2b;
    --brand-grey: #555558;
  }
  html, body { margin: 0; padding: 0; overflow: hidden; }
  .flyer {
    position: relative;
    width: 1200px;
    height: 2400px;
    overflow: hidden;
    background: var(--paper);
    font-family: "Open Sans", sans-serif;
  }
  .flyer__shapes { position: absolute; inset: 0; width: 1200px; height: 2400px; }
  .brand { position: absolute; left: 0; top: 0; width: 1200px; height: 320px; }
  .brand__dot {
    position: absolute; left: 130px; top: 95px; width: 170px; height: 170px;
    border-radius: 50%; background: var(--red);
  }
  .brand__name {
    position: absolute; left: 345px; top: 70px; margin: 0;
    font-family: "Montserrat", sans-serif; font-weight: 500;
    font-size: 92px; line-height: 92px; color: var(--brand-grey);
    letter-spacing: -1px;
  }
  .brand__tagline {
    position: absolute; left: 355px; top: 258px; margin: 0;
    font-family: "Lora", serif; font-style: italic;
    font-size: 36px; color: var(--ink);
  }
  .headline {
    position: absolute; left: 56px; top: 1188px; margin: 0;
    font-family: "Roboto", sans-serif; font-weight: 500;
    font-size: 40px; line-height: 58px; letter-spacing: 2px;
    color: var(--white); text-transform: uppercase;
  }
  .pitch {
    position: absolute; left: 50px; width: 1100px; margin: 0; text-align: center;
  }
  .pitch--lead { top: 1420px; font-size: 42px; line-height: 60px; color: var(--red); }
  .pitch--service { top: 1635px; font-size: 38px; line-height: 66px; color: var(--ink); }
  .pitch--service span { display: block; font-size: 33px; letter-spacing: -0.5px; }
  .modules {
    position: absolute; left: 445px; top: 1768px; width: 640px; margin: 0; padding: 0;
    list-style: none; font-size: 41px; line-height: 44px; color: var(--red); letter-spacing: 1px;
  }
  .modules li { text-align: justify; text-align-last: justify; }
  .setup {
    position: absolute; left: 358px; top: 1980px; margin: 0;
    font-size: 40px; color: var(--ink);
  }
  .contact {
    position: absolute; left: 142px; top: 2198px; margin: 0;
    font-family: "Quicksand", sans-serif; font-weight: 700;
    font-size: 42px; line-height: 57px; color: var(--ink); letter-spacing: 1.5px;
  }
  .contact span { display: block; }
  .phone {
    position: absolute; left: 855px; top: 2302px; margin: 0;
    font-family: "Roboto", sans-serif; font-weight: 500;
    font-size: 46px; color: var(--white);
  }
</style>
</head>
<body>
<main class="flyer">
  <svg class="flyer__shapes" viewBox="0 0 700 1400" preserveAspectRatio="none" aria-hidden="false">
    <defs>
      <linearGradient id="metal" x1="0" y1="0" x2="1" y2="0">
        <stop offset="0" stop-color="#7e868d"/>
        <stop offset="0.5" stop-color="#c3c8cd"/>
        <stop offset="1" stop-color="#8c949b"/>
      </linearGradient>
      <linearGradient id="desk" x1="0" y1="0" x2="1" y2="1">
        <stop offset="0" stop-color="#9aa5ad"/>
        <stop offset="0.6" stop-color="#b7c0c6"/>
        <stop offset="1" stop-color="#c9cfd3"/>
      </linearGradient>
      <linearGradient id="footMetal" x1="0" y1="0" x2="0" y2="1">
        <stop offset="0" stop-color="#c6cbcf"/>
        <stop offset="1" stop-color="#8f979e"/>
      </linearGradient>
    </defs>
    <!-- soft diagonal wash behind body copy -->
    <polygon points="330,800 700,1000 700,1230 560,1230 120,800" fill="#e1e2e6"/>
    <!-- metal panel -->
    <rect class="metal-panel" x="0" y="265" width="320" height="415" fill="url(#metal)"/>
    <!-- diagonal bands -->
    <polygon class="band-pink" points="0,192 62,192 358,680 250,680 0,270" fill="var(--pink)"/>
    <polygon class="band-red" points="62,215 170,215 455,680 355,680" fill="var(--red)"/>
    <!-- desk scene -->
    <polygon role="img" aria-label="Photo of a business desk with a newspaper, laptop, plant, cards and notebook" points="170,215 700,215 700,660 448,660" fill="url(#desk)"/>
    <rect x="440" y="660" width="260" height="22" fill="var(--pink)"/>
    <!-- heading band -->
    <polygon class="band-heading" points="0,683 700,683 700,705 540,705 510,800 0,800" fill="var(--red)"/>
    <!-- footer bands -->
    <polygon points="0,1218 520,1218 580,1290 700,1290 700,1400 0,1400" fill="var(--pink)"/>
    <polygon points="0,1240 515,1240 575,1300 700,1300 700,1400 0,1400" fill="var(--red)"/>
    <polygon points="0,1268 400,1268 470,1400 0,1400" fill="var(--white)"/>
    <polygon points="0,1276 395,1276 462,1400 0,1400" fill="url(#footMetal)"/>
  </svg>

  <header class="brand">
    <div class="brand__dot"></div>
    <h1 class="brand__name">Tally Your<br>Ledger Free</h1>
    <p class="brand__tagline">It's easy enough to do yourself</p>
  </header>

  <h2 class="headline">Starting a new business ?<br>Want to save on bookkeeping<br>fees for your existing business?</h2>

  <p class="pitch pitch--lead">You can now save 1000's off bookkeeping fees by<br>Doing it Yourself. Using our Bookkeeper coftware<br>you simply key in the information as you go.</p>

  <p class="pitch pitch--service">We offer one on one training, backup and support.<span>We can assist you with BAS Preparation and Payrol Advice.</span></p>

  <ul class="modules">
    <li>Add Modules as required:</li>
    <li>Point of Sale Module</li>
    <li>Jobs Management Module</li>
    <li>Website Intergration Module</li>
  </ul>

  <p class="setup">Fee set up assistance and training.</p>

  <p class="contact">
    <span>www.tylfr.com.au</span>
    <span>admin@tylfr.com.au</span>
    <span>Lets get the ball rolling:</span>
  </p>
  <p class="phone">1300 642 815</p>
</main>
</body>
</html>
```